Very visible CoWorking Building Sign overlooking downtown LA and 110 freeway

Our building is drab but very visible and in the best location. We need a great sign for our monolith that overlooks downtown LA and the 100 freeway. We are a new CoWorking business and would like to have a few things we do on the sign: private offices, virtual offices, CoWorking Lounge. Everything we have seen is ho-hum. Can you get us noticed? We need people to know what we do and that we are here but in a creative, professional, unique sign.
Target Market(s)
People who have a business in DTLA, remote workers and those who work from home who need a professional address.
Requirements
Must have
- Our logo (which can be somewhat reimagined) which has our address 2740 on it. The three things we focus on: Private Offices, Virtual Offices, CoWorking Lounge. Incorporate some Navy. Readable from several hundred feet away.
Nice to have
- Mural feel? Something inspirational in this crazy COVID times? Graphics? Color block. I like the idea of decorative but it has to be readable as a building sign. The same with the use of colors. Our colors are grays and navy but with a pop of the chartreuse (we have 2 velvet chartreuse chairs in the space). Helpful to view our website: Halvorn2740.com.
Should not have
- Not too graffiti. Keep it professional but unique and wow.

```html
<!DOCTYPE html>
<html lang="en">
<head>
<meta charset="utf-8">
<title>Halvorn 2740 Building Sign</title>
<link href="https://fonts.googleapis.com/css2?family=Montserrat:wght@500;600;700&display=swap" rel="stylesheet">
<style>
  :root {
    --navy: #1b355e;
    --accent-blue: #2166b0;
    --chartreuse: #8cc63f;
    --white: #ffffff;
    --backdrop: #5b5b5b;
  }
  * { margin: 0; padding: 0; box-sizing: border-box; }
  html, body {
    width: 1200px;
    height: 1091px;
    overflow: hidden;
    background: var(--backdrop);
  }
  .canvas {
    position: relative;
    width: 1200px;
    height: 1091px;
  }
  .sign {
    position: absolute;
    left: 50px;
    top: 435px;
    width: 1100px;
    height: 220px;
    font-family: "Montserrat", sans-serif;
  }
  .sign-shapes {
    position: absolute;
    inset: 0;
  }
  .web-address {
    position: absolute;
    left: 274px;
    top: 39px;
    width: 264px;
    height: 38px;
    display: flex;
    align-items: center;
    justify-content: center;
    color: var(--white);
    font-weight: 500;
    font-size: 17px;
    letter-spacing: 0.5px;
  }
  .wordmark {
    position: absolute;
    left: 46px;
    top: 108px;
    color: var(--navy);
    font-weight: 600;
    font-size: 50px;
    line-height: 1;
    letter-spacing: 1px;
    white-space: nowrap;
  }
  .services {
    position: absolute;
    left: 590px;
    top: 0;
    height: 220px;
    list-style: none;
    display: flex;
    flex-direction: column;
    justify-content: center;
    gap: 16px;
  }
  .service {
    display: flex;
    align-items: center;
    gap: 12px;
    color: var(--white);
    font-weight: 700;
    font-size: 35px;
    line-height: 43px;
    letter-spacing: 1px;
    white-space: nowrap;
  }
  .service-marker {
    width: 22px;
    height: 26px;
    flex: none;
  }
</style>
</head>
<body>
<div class="canvas">
  <section class="sign" aria-label="Halvorn 2740 coworking building sign">
    <svg class="sign-shapes" width="1100" height="220" viewBox="0 0 1100 220" aria-hidden="true">
      <rect class="panel-light" x="0" y="0" width="1100" height="220" fill="var(--white)"/>
      <polygon class="panel-navy" points="571,0 1100,0 1100,220 492,220" fill="var(--navy)"/>
      <polygon class="accent-stripe" points="556,0 568,0 511,160 501,150" fill="var(--accent-blue)"/>
      <polygon class="web-band" points="268,39 538,39 538,77 256,77" fill="var(--chartreuse)"/>
    </svg>

    <div class="web-address">www.halvorn2740.com</div>
    <div class="wordmark">2740 HALVORN</div>

    <ul class="services">
      <li class="service">
        <svg class="service-marker" viewBox="0 0 22 26" aria-hidden="true">
          <polyline points="2,3 10,13 2,23" fill="none" stroke="var(--chartreuse)" stroke-width="3.5"/>
          <polyline points="11,3 19,13 11,23" fill="none" stroke="var(--chartreuse)" stroke-width="3.5"/>
        </svg>
        PRIVATE OFFICES
      </li>
      <li class="service">
        <svg class="service-marker" viewBox="0 0 22 26" aria-hidden="true">
          <polyline points="2,3 10,13 2,23" fill="none" stroke="var(--chartreuse)" stroke-width="3.5"/>
          <polyline points="11,3 19,13 11,23" fill="none" stroke="var(--chartreuse)" stroke-width="3.5"/>
        </svg>
        VIRTUAL OFFICES
      </li>
      <li class="service">
        <svg class="service-marker" viewBox="0 0 22 26" aria-hidden="true">
          <polyline points="2,3 10,13 2,23" fill="none" stroke="var(--chartreuse)" stroke-width="3.5"/>
          <polyline points="11,3 19,13 11,23" fill="none" stroke="var(--chartreuse)" stroke-width="3.5"/>
        </svg>
        COWORKING LOUNGE
      </li>
    </ul>
  </section>
</div>
</body>
</html>
```